Brightmark Pixel Collective Website

I need my website redesigned to look very modern with the latest services. Check out my old website for information: www.brightmarkpixelcollective.com

You can use the same site menu links

It doesn't need to have the Recent News section

Please use the yellow, black and grey color scheme

Target Market(s)

25-50 years in range. Small Business Owners

Industry/Entity Type

Group

Requirements
Must have
• Logo and similar color scheme to current website
• Modern, Modern, Modern! I want a very fresh and modern look
Should not have
• Boring Look

```html
<!DOCTYPE html>
<html lang="en">
<head>
<meta charset="utf-8">
<title>Brightmark Pixel Collective</title>
<link href="https://fonts.googleapis.com/css2?family=Open+Sans:wght@300;400;600;700&display=swap" rel="stylesheet">
<style>
:root{
  --ink:#1c1c1c;
  --header:#222;
  --orange:#f5a612;
  --yellow:#f7c93a;
  --yellow-soft:#f3cc4a;
  --slate:#3d4a50;
  --light:#f1f1f1;
  --grey:#e4e4e4;
  --text:#555;
  --footer:#2e2e2e;
  --footer-bottom:#1d1d1d;
}
*{box-sizing:border-box;margin:0;padding:0}
html,body{width:806px;height:1200px;overflow:hidden}
body{font-family:"Open Sans",Arial,sans-serif;color:var(--text);position:relative;background:var(--light)}
.abs{position:absolute}

.site-header{left:0;top:0;width:806px;height:50px;background:linear-gradient(#2c2c2c,#111)}
.brand{left:166px;top:14px;display:flex;align-items:center;gap:8px;color:#e8e8e8;font-size:14px;font-weight:300;letter-spacing:.3px}
.brand-mark{width:20px;height:20px;background:var(--orange)}
.contact-lines{left:456px;top:16px;display:flex;gap:7px;align-items:center;font-size:7px;color:#ccc;font-weight:600;line-height:10px}
.contact-lines b{color:var(--orange)}
.quote-btn{left:569px;top:15px;width:74px;height:22px;border:1px solid #666;background:linear-gradient(#555,#333);color:#fff;font-size:7.5px;font-weight:700;display:flex;align-items:center;justify-content:center;border-radius:2px}
.quote-btn span{color:var(--orange);margin:0 2px}

.main-nav{left:0;top:50px;width:806px;height:22px;background:linear-gradient(#f9b624,#e99a08)}
.main-nav a{position:absolute;top:6px;color:#fff;font-size:8px;font-weight:600;text-decoration:none;text-transform:uppercase}

.hero{left:0;top:72px;width:806px;height:204px;background:linear-gradient(120deg,#4a3a5a 0%,#6e5a7a 30%,#8a7c86 55%,#5a4a66 80%,#3a2e4a 100%)}
.slide-arrow{width:22px;height:22px;border-radius:50%;display:flex;align-items:center;justify-content:center;color:#fff;font-size:10px}
.slide-arrow.prev{left:138px;top:166px;background:#444}
.slide-arrow.next{left:644px;top:166px;background:var(--orange)}

.tagline{left:0;top:276px;width:806px;height:53px;background:radial-gradient(ellipse at 50% 50%,#56646a,var(--slate));text-align:center;color:#fff}
.tagline h1{font-size:12.5px;font-weight:600;margin-top:11px}
.tagline h1 em{font-style:normal;color:var(--yellow)}
.tagline p{font-size:9px;color:#d8dde0;font-weight:400}

.services{left:0;top:329px;width:806px;height:91px;background:var(--yellow)}
.service{position:absolute;top:0;height:91px;text-align:center;color:#5a4410}
.service + .service{border-left:1px solid #d9a928}
.service svg{display:block;margin:16px auto 0}
.service h3{font-size:12.5px;font-weight:300;color:#6a5010;margin-top:4px}
.service p{font-size:6px;text-transform:uppercase;color:#6a5010}

.works{left:0;top:420px;width:806px;height:325px;background:var(--light)}
.section-title{position:absolute;left:166px;width:474px;text-align:center;font-size:12px;font-weight:400;color:#666;text-transform:uppercase;border-bottom:1px solid #ccc;padding-bottom:6px}
.work{position:absolute;width:111px;height:105px;border:2px solid #ddd;background:#ccc}
.work .thumb{position:absolute;inset:0}
.work .cap{position:absolute;left:0;right:0;bottom:10px;text-align:center;color:#fff}
.work .cap b{display:block;font-size:9px;font-weight:400}
.work .cap i{display:block;font-style:normal;font-size:5.5px;color:#ddd;text-transform:uppercase}

.why{left:0;top:745px;width:806px;height:210px;background:var(--grey)}
.feature{position:absolute;width:112px}
.feature .head{display:flex;align-items:center;gap:6px;font-size:7px;font-weight:700;color:#333;text-transform:uppercase}
.feature .ico{width:20px;height:20px;border-radius:50%;background:#3a3a3a;display:flex;align-items:center;justify-content:center}
.feature p{font-size:6.5px;line-height:10px;color:#555;margin-top:6px}

.noticed{left:0;top:955px;width:806px;height:131px;background:linear-gradient(90deg,#f4cf4e,#f0c535)}
.noticed h2{position:absolute;left:166px;top:17px;font-size:12.5px;font-weight:300;color:#5a4410}
.noticed .lead{position:absolute;left:166px;top:41px;font-size:6.5px;font-weight:700;color:#4a3810}
.noticed .body{position:absolute;left:166px;top:61px;width:310px;font-size:6.5px;line-height:10px;color:#4a3810}
.read-more{position:absolute;left:165px;top:98px;width:52px;height:16px;border-radius:3px;background:#f7f2e0;border:1px solid #e0d6b0;font-size:5px;font-weight:600;color:#555;display:flex;align-items:center;justify-content:center}
.video{position:absolute;left:489px;top:18px;width:147px;height:97px;background:linear-gradient(160deg,#1d2a2a,#3a4a3c 60%,#101616)}
.video .vtitle{position:absolute;left:5px;top:3px;font-size:5.5px;color:#fff}
.video .play{position:absolute;left:65px;top:40px;width:16px;height:16px;border-radius:50%;background:rgba(0,0,0,.6)}
.video .bar{position:absolute;left:0;bottom:0;width:100%;height:10px;background:#111}

.site-footer{left:0;top:1086px;width:806px;height:91px;background:var(--footer)}
.footer-brand{position:absolute;left:190px;top:36px;display:flex;align-items:center;gap:6px;color:#ddd;font-size:8px;font-weight:600;width:100px;line-height:10px}
.footer-brand .sq{width:14px;height:14px;background:var(--orange);flex:none}
.fcol{position:absolute;top:17px;color:#fff}
.fcol h4{font-size:7.5px;font-weight:700;margin-bottom:6px}
.fcol li{list-style:none;font-size:5.5px;color:#999;line-height:12px}
.fcol li::before{content:"› ";color:#888}
.fcol li.on{color:var(--orange)}
.fcol.contact li::before{content:""}
.social{display:flex;gap:6px}
.social span{width:18px;height:18px;border-radius:2px;background:#3a6fb0}
.legal{left:0;top:1177px;width:806px;height:23px;background:var(--footer-bottom);font-size:5.5px;color:#888}
.legal .l{position:absolute;left:161px;top:8px}
.legal .r{position:absolute;left:571px;top:8px}
</style>
</head>
<body>

<header class="site-header abs">
  <div class="brand abs"><span class="brand-mark"></span>Brightmark Pixel Collective</div>
  <div class="contact-lines abs">
    <svg width="18" height="18" viewBox="0 0 18 18"><circle cx="9" cy="9" r="8" fill="none" stroke="#999" stroke-width="1.2"/><path d="M6 5l2 0 1 2-1 1a5 5 0 0 0 2 2l1-1 2 1 0 2c-4 0-7-3-7-7z" fill="#999"/></svg>
    <div>Local: <b>555-014-2200</b><br>Toll Free: <b>1-800-555-0187</b></div>
  </div>
  <div class="quote-btn abs">Request<span>FREE</span>Quote</div>
</header>

<nav class="main-nav abs">
  <a style="left:179px">Home</a>
  <a style="left:246px">Web Design</a>
  <a style="left:339px">Search Engine Marketing</a>
  <a style="left:495px">Social Media</a>
  <a style="left:596px">Contact</a>
</nav>

<section class="hero abs" role="img" aria-label="Night city traffic photo with three monitors showing client websites">
  <div class="slide-arrow prev abs">‹</div>
  <div class="slide-arrow next abs">›</div>
</section>

<section class="tagline abs">
  <h1>We are an <em>award winning</em> web design &amp; internet marketing company</h1>
  <p>Suspendisse tristique ante sit amet sem pulvinar posuere.</p>
</section>

<section class="services abs">
  <div class="service" style="left:161px;width:161px">
    <svg width="46" height="32" viewBox="0 0 46 32"><rect x="6" y="2" width="34" height="23" rx="2" fill="none" stroke="#3a3a3a" stroke-width="3"/><rect x="1" y="26" width="44" height="4" rx="1" fill="#3a3a3a"/></svg>
    <h3>Web Design</h3><p>It was hard to make it so cool</p>
  </div>
  <div class="service" style="left:322px;width:161px">
    <svg width="36" height="34" viewBox="0 0 36 34"><path d="M10 32v-8c-5-3-7-8-5-13 2-6 9-9 15-8 7 1 11 7 10 13l3 5h-3v4c0 2-2 3-4 3h-3v4" fill="none" stroke="#3a3a3a" stroke-width="2"/><circle cx="15" cy="13" r="4" fill="none" stroke="#3a3a3a" stroke-width="2"/><circle cx="23" cy="18" r="3" fill="none" stroke="#3a3a3a" stroke-width="2"/></svg>
    <h3>Internet Marketing</h3><p>It was fun to make it so cool</p>
  </div>
  <div class="service" style="left:483px;width:161px">
    <svg width="36" height="34" viewBox="0 0 36 34"><circle cx="18" cy="7" r="4" fill="none" stroke="#3a3a3a" stroke-width="2"/><circle cx="9" cy="16" r="4" fill="#3a3a3a"/><circle cx="27" cy="16" r="4" fill="#3a3a3a"/><path d="M2 33v-7a7 7 0 0 1 14 0v7zM20 33v-7a7 7 0 0 1 14 0v7z" fill="#3a3a3a"/></svg>
    <h3>Social Media</h3><p>It is cool to keep it so cool</p>
  </div>
</section>

<section class="works abs">
  <h2 class="section-title" style="top:20px">Our Recent Works</h2>
  <div class="work" style="left:166px;top:62px"><div class="thumb" role="img" aria-label="Printing company website screenshot" style="background:linear-gradient(#c8202a 0%,#e8e8e8 45%,#555 100%)"></div><div class="cap"><b>Project Title</b><i>Graphic Design</i></div></div>
  <div class="work" style="left:287px;top:62px"><div class="thumb" role="img" aria-label="Outdoor event website screenshot" style="background:linear-gradient(#d0601a,#7a3018 50%,#555)"></div><div class="cap"><b>Project Title</b><i>Graphic Design</i></div></div>
  <div class="work" style="left:408px;top:62px"><div class="thumb" role="img" aria-label="Pet care website screenshot" style="background:linear-gradient(#5a5040,#7a6a48 50%,#6a6a50)"></div><div class="cap"><b>Project Title</b><i>Graphic Design</i></div></div>
  <div class="work" style="left:529px;top:62px"><div class="thumb" role="img" aria-label="Restaurant website screenshot" style="background:linear-gradient(#6a6a6a,#b09070 55%,#3a2a20)"></div><div class="cap"><b>Project Title</b><i>Graphic Design</i></div></div>
  <div class="work" style="left:166px;top:184px"><div class="thumb" role="img" aria-label="Hair salon website screenshot" style="background:linear-gradient(#4a5a2a,#6a6a3a 60%,#3a3a2a)"></div><div class="cap"><b>Project Title</b><i>Graphic Design</i></div></div>
  <div class="work" style="left:287px;top:184px"><div class="thumb" role="img" aria-label="Home store website screenshot" style="background:linear-gradient(#1a6a4a,#1a2a2a 50%,#1a3a7a)"></div><div class="cap"><b>Project Title</b><i>Graphic Design</i></div></div>
  <div class="work" style="left:408px;top:184px"><div class="thumb" role="img" aria-label="Landscaping website screenshot" style="background:linear-gradient(#2a4a9a,#2a3a3a 45%,#5a7a4a)"></div><div class="cap"><b>Project Title</b><i>Graphic Design</i></div></div>
  <div class="work" style="left:529px;top:184px"><div class="thumb" role="img" aria-label="Sports team website screenshot" style="background:linear-gradient(#3a3a3a,#6a6a5a 55%,#2a2a2a)"></div><div class="cap"><b>Project Title</b><i>Graphic Design</i></div></div>
</section>

<section class="why abs">
  <h2 class="section-title" style="top:17px">Why Choose Us</h2>
  <div class="feature" style="left:166px;top:56px"><div class="head"><span class="ico"><svg width="10" height="10" viewBox="0 0 10 10"><circle cx="5" cy="5" r="3.5" fill="none" stroke="#fff" stroke-width="1.3"/></svg></span>Customer Support</div><p>Select design work for delivery in a beautiful, simple email to clients or teammates.</p></div>
  <div class="feature" style="left:287px;top:56px"><div class="head"><span class="ico"><svg width="10" height="10" viewBox="0 0 10 10"><rect x="2" y="2" width="6" height="6" fill="none" stroke="#fff" stroke-width="1.3"/></svg></span>Responsive</div><p>Lorem ipsum dolor sit amet, tetur adipiscing elit. Suspendisse smod congue bibendum.</p></div>
  <div class="feature" style="left:408px;top:56px"><div class="head"><span class="ico"><svg width="10" height="10" viewBox="0 0 10 10"><circle cx="5" cy="5" r="4" fill="none" stroke="#fff" stroke-width="1.1"/><path d="M1 5h8M5 1v8" stroke="#fff" stroke-width="1"/></svg></span>Multilanguage</div><p>Select design work for delivery in a beautiful, simple email to clients or teammates.</p></div>
  <div class="feature" style="left:529px;top:56px"><div class="head"><span class="ico"><svg width="10" height="10" viewBox="0 0 10 10"><path d="M5 1l4 7H1z" fill="#fff"/></svg></span>Web Development</div><p>Aliquam erat volutpat. Phasellus eget justo lacus. Vivamus pharetra ullamcorper massa.</p></div>
  <div class="feature" style="left:166px;top:129px"><div class="head"><span class="ico"><svg width="10" height="10" viewBox="0 0 10 10"><rect x="2" y="1" width="6" height="8" fill="none" stroke="#fff" stroke-width="1.2"/></svg></span>Well Documented</div><p>Because we know you don't want to be limited on a portrait or scape format we made Showcase.</p></div>
  <div class="feature" style="left:287px;top:129px"><div class="head"><span class="ico"><svg width="10" height="10" viewBox="0 0 10 10"><path d="M2 8l6-6" stroke="#fff" stroke-width="1.6"/></svg></span>Unlimited Colors</div><p>With just a few clicks you can add any color you want.compatible in both portrait AND landscape!</p></div>
  <div class="feature" style="left:408px;top:129px"><div class="head"><span class="ico"><svg width="10" height="10" viewBox="0 0 10 10"><path d="M4 2L1 5l3 3M6 2l3 3-3 3" fill="none" stroke="#fff" stroke-width="1.2"/></svg></span>HTML5 &amp; CSS3</div><p>With just a few clicks you can add any color you want.compatible in both portrait AND landscape!</p></div>
  <div class="feature" style="left:529px;top:129px"><div class="head"><span class="ico"><svg width="10" height="10" viewBox="0 0 10 10"><path d="M2 1v8M4 1v8M6 1v8M8 1v8" stroke="#fff" stroke-width="1"/></svg></span>Customization</div><p>Aliquam erat volutpat. Phasellus eget justo lacus. Vivamus pharetra ullamcorper massa.</p></div>
</section>

<section class="noticed abs">
  <h2>Brightmark Pixel Collective will get you noticed</h2>
  <p class="lead">We are an award winning web design &amp; internet marketing company located in Harborview.</p>
  <p class="body">As a Harborview Web Design company, we create web sites to what our clients want and that's found in our marketing. Here at Brightmark Pixel Collective, we not only design you a first class web presence but market your website so your buyer finds you first before anyone else</p>
  <div class="read-more">READ MORE</div>
  <div class="video" role="img" aria-label="Company video player still">
    <span class="vtitle">Harborview Web Design</span>
    <span class="play"></span>
    <span class="bar"></span>
  </div>
</section>

<footer class="site-footer abs">
  <div class="footer-brand"><span class="sq"></span>Brightmark Pixel Collective</div>
  <div class="fcol" style="left:283px"><h4>Navigation</h4><ul><li>Home</li><li>About</li><li>Services</li><li>Contact</li></ul></div>
  <div class="fcol" style="left:364px"><h4>Services</h4><ul><li class="on">Web Design</li><li>Graphic Design</li><li>SEO Marketing</li><li>Social MEdia</li></ul></div>
  <div class="fcol contact" style="left:445px"><h4>Contact Us</h4><ul><li>☏ &nbsp;+1800-123-4567</li><li>✉ &nbsp;info@yourwebsite.com</li><li>⌖ &nbsp;Your Address, Your Country</li><li>&nbsp;&nbsp;&nbsp;Your Zip Code</li></ul></div>
  <div class="fcol" style="left:554px"><h4>Social</h4><div class="social" aria-label="Social network links"><span></span><span style="background:#2fa0d8"></span><span style="background:#1f6aa0"></span><span style="background:#d84a38"></span></div></div>
</footer>

<div class="legal abs"><span class="l">Copyright 2014 © CompanyName - All Rights Reserved</span><span class="r">Site Map &nbsp;•&nbsp; Privacy Policy</span></div>

</body>
</html>
```